Marine Services Letterhead design

We need a letterhead design for an Australian owned company in Victoria named K+K Harbour Works Pty Ltd. We provide linesmen and launches to assist the large ships that come into port.
Our colour is orange.
The final design should have a strong nautical theme and communicate safety and reliability.
I would like to use the letter head on invoices so it should print to pdf well.

Target Market(s)

Owners and representatives of shipping companies. It is not for general public

Industry/Entity Type

Nautical

Requirements
Must have
• A shipping theme, not overly complicated, featuring safety orange colours but not all orange of course.
The letterhead should just sit at the top of the page so I can use for invoices.
Nice to have
• Something elegant and stylish
Should not have
• cartoons or pop art

```html
<!DOCTYPE html>
<html lang="en">
<head>
<meta charset="utf-8">
<title>K+K Harbour Works Letterhead</title>
<link href="https://fonts.googleapis.com/css2?family=Ubuntu:wght@400;500&display=swap" rel="stylesheet">
<style>
  :root {
    --backdrop: #ececec;
    --paper: #f8f8f8;
    --ink: #8a8a8a;
    --ink-dark: #5f5f5f;
    --sea-green: #93b8a0;
    --safety-orange: #e1a86a;
    --watermark: #ececec;
    --signature-fill: #eeeeee;
  }
  * { box-sizing: border-box; margin: 0; padding: 0; }
  html, body {
    width: 1200px;
    height: 1000px;
    overflow: hidden;
    background: var(--backdrop);
    font-family: "Ubuntu", Arial, sans-serif;
  }
  .letterhead {
    position: absolute;
    left: 275px;
    top: 40px;
    width: 650px;
    height: 920px;
    background: var(--paper);
    box-shadow: 0 4px 18px rgba(0,0,0,0.08);
    overflow: hidden;
  }
  .brand-mark {
    position: absolute;
    top: 70px;
    right: 60px;
    display: flex;
    align-items: center;
    gap: 10px;
  }
  .brand-mark__square {
    width: 22px;
    height: 22px;
    background: var(--safety-orange);
  }
  .brand-mark__name {
    font-size: 16px;
    font-weight: 500;
    color: var(--safety-orange);
    letter-spacing: 0.3px;
  }
  .watermark-name {
    position: absolute;
    left: 90px;
    top: 560px;
    width: 420px;
    text-align: center;
    font-size: 40px;
    font-weight: 500;
    color: var(--watermark);
    white-space: nowrap;
  }
  .letter-body {
    position: absolute;
    left: 80px;
    top: 160px;
    width: 490px;
    font-size: 11px;
    line-height: 1.7;
    color: var(--ink);
  }
  .letter-body p { margin-bottom: 16px; }
  .letter-body .greeting { margin-bottom: 10px; }
  .letter-body .paragraph { text-indent: 22px; text-align: justify; }
  .signature {
    position: absolute;
    left: 330px;
    top: 640px;
    width: 170px;
    height: 56px;
    background: var(--signature-fill);
    border-radius: 4px;
  }
  .footer-contact {
    position: absolute;
    left: 30px;
    bottom: 42px;
    color: var(--ink-dark);
  }
  .footer-contact__company {
    font-size: 13px;
    font-weight: 500;
    color: var(--sea-green);
    margin-bottom: 4px;
  }
  .footer-contact__line {
    display: flex;
    align-items: center;
    gap: 5px;
    font-size: 9px;
    line-height: 1.5;
  }
  .footer-contact__line svg { width: 8px; height: 8px; fill: var(--ink-dark); }
  .footer-bands {
    position: absolute;
    left: 0;
    right: 0;
    bottom: 12px;
    height: 12px;
    display: flex;
    gap: 5px;
  }
  .footer-bands__green { width: 190px; background: var(--sea-green); }
  .footer-bands__orange { flex: 1; background: var(--safety-orange); }
</style>
</head>
<body>
  <main class="letterhead">
    <div class="brand-mark">
      <span class="brand-mark__square"></span>
      <span class="brand-mark__name">K+K Harbour Works</span>
    </div>

    <div class="watermark-name" aria-hidden="true">K+K Harbour Works</div>

    <section class="letter-body">
      <p class="greeting">Dear Client,</p>
      <p class="paragraph">Lorem ipsum dolor sit amet, consectetur adipiscing elit. Nulla sodales nisi vitae lorem ipsum dolor sit amet, consectetur adipiscing elit. Suspendisse feugiat eros nisl, a facilisis risus eleifend sed. Aliquam mauris enim, fermentum eu lacinia sit amet, laoreet eu leo. Nullam eleifend nulla in libero tristique, ac vulputate odio tincidunt. Etiam non condimentum tortor. Integer suscipit neque nec odio porttitor cursus. Phasellus a sapien blandit, suscipit justo id, condimentum ante.</p>
      <p class="paragraph">Nulla tincidunt molestie libero vel pretium. Donec condimentum nulla sit amet risus semper imperdiet. Duis congue eros nec diam blandit, et pellentesque sapien auctor. Curabitur iaculis enim lectus, in imperdiet mauris mattis eget. Etiam ac ornare metus. Mauris risus leo, egestas at dolor a, ultrices viverra est.</p>
      <p class="paragraph">Nullam auctor venenatis metus, eu pulvinar sapien dapibus non. Cum sociis natoque penatibus et magnis dis parturient montes, nascetur ridiculus mus. Praesent sed lorem eget tortor volutpat dictum vel vel ipsum. Morbi ac mauris sed elit dictum volutpat.</p>
      <p>Best regards,</p>
    </section>

    <div class="signature" role="img" aria-label="Space for a handwritten signature"></div>

    <footer class="footer-contact">
      <div class="footer-contact__company">K+K Harbour Works Pty Ltd</div>
      <div class="footer-contact__line">
        <svg viewBox="0 0 10 10" aria-hidden="true"><path d="M5 0a3.5 3.5 0 0 0-3.5 3.5C1.5 6 5 10 5 10s3.5-4 3.5-6.5A3.5 3.5 0 0 0 5 0zm0 5a1.5 1.5 0 1 1 0-3 1.5 1.5 0 0 1 0 3z"/></svg>
        PO Box 214 Portside 3990
      </div>
      <div class="footer-contact__line">
        <svg viewBox="0 0 10 10" aria-hidden="true"><path d="M2 0.5l2 2.2-1 1.2c.6 1.3 1.6 2.3 2.9 2.9l1.2-1 2.2 2-1.2 1.7C4 9.3.7 6 .3 1.7z"/></svg>
        1300 000 417
      </div>
      <div class="footer-contact__line">
        <svg viewBox="0 0 10 10" aria-hidden="true"><path d="M1 3h8v5H1zM2.5 0.5h5V3h-5zM2.5 5h5v1h-5z"/></svg>
        0400 118 266
      </div>
    </footer>

    <div class="footer-bands">
      <span class="footer-bands__green"></span>
      <span class="footer-bands__orange"></span>
    </div>
  </main>
</body>
</html>
```